Bref créative
Business Cards - Skyline Assessors
Two sided business cards
Simple
Corwin Hask
Certified Appraiser
48270 Millbrook Lane #1174
Sterling, VA 20391
corwin@plumvexa.com
www.plumvexa.com
Just the logo, either include the text or not (what ever looks better)
Colors and Fonts Guide

```html
<!DOCTYPE html>
<html lang="en">
<head>
<meta charset="utf-8">
<title>Skyline Assessors – Business Card</title>
<link rel="stylesheet" href="https://fonts.googleapis.com/css2?family=Arimo:wght@400;700&display=swap">
<style>
  :root {
    --page-bg: #e9e7e4;
    --card-bg: #ffffff;
    --card-edge: #f1f1f3;
    --brand-navy: #1f3550;
    --accent-red: #b5202a;
    --text-dark: #2b2b2b;
    --text-mid: #444444;
  }
  * { box-sizing: border-box; margin: 0; padding: 0; }
  html, body {
    width: 1200px; height: 780px; overflow: hidden;
    background: var(--page-bg);
    font-family: "Arimo", Arial, sans-serif;
  }
  .canvas {
    position: relative; width: 1200px; height: 780px;
    display: flex; align-items: center; justify-content: center;
  }
  .business-card {
    position: relative; width: 1050px; height: 600px;
    background: linear-gradient(180deg, var(--card-bg) 0%, var(--card-edge) 100%);
    border-radius: 44px;
    box-shadow: 0 10px 30px rgba(0,0,0,0.18);
  }
  .brand {
    position: absolute; left: 56px; top: 120px;
    display: flex; align-items: center; gap: 16px;
  }
  .brand-dot {
    width: 30px; height: 30px; border-radius: 50%;
    background: var(--brand-navy);
  }
  .brand-name {
    font-size: 46px; font-weight: 700; color: var(--brand-navy);
    letter-spacing: 0.5px;
  }
  .address {
    position: absolute; left: 58px; top: 228px;
    font-size: 23px; line-height: 30px; color: var(--text-dark);
  }
  .contact-list {
    position: absolute; left: 58px; top: 318px;
    list-style: none;
  }
  .contact-item {
    display: flex; align-items: center; gap: 12px;
    font-size: 22px; line-height: 34px; color: var(--text-mid);
  }
  .contact-icon { width: 24px; height: 24px; flex: none; }
  .person {
    position: absolute; right: 60px; top: 132px; text-align: right;
  }
  .person-name {
    font-size: 31px; font-weight: 700; color: var(--accent-red);
  }
  .person-title {
    margin-top: 8px; font-size: 22px; font-weight: 700; color: var(--text-mid);
  }
</style>
</head>
<body>
<main class="canvas">
  <section class="business-card">
    <div class="brand">
      <span class="brand-dot"></span>
      <span class="brand-name">Skyline Assessors</span>
    </div>

    <address class="address" style="font-style:normal">
      48270 Millbrook Lane #1174<br>
      Sterling, VA 20391
    </address>

    <ul class="contact-list">
      <li class="contact-item">
        <svg class="contact-icon" viewBox="0 0 24 24" aria-hidden="true">
          <circle cx="12" cy="12" r="12" fill="var(--accent-red)"/>
          <rect x="8.5" y="5" width="7" height="14" rx="1.5" fill="#fff"/>
          <rect x="9.8" y="7" width="4.4" height="7" fill="var(--accent-red)"/>
        </svg>
        5718830264
      </li>
      <li class="contact-item">
        <svg class="contact-icon" viewBox="0 0 24 24" aria-hidden="true">
          <circle cx="12" cy="12" r="12" fill="var(--accent-red)"/>
          <circle cx="12" cy="12" r="2.6" fill="none" stroke="#fff" stroke-width="1.8"/>
          <path d="M14.6 9.5v3.6c0 1.6 2.6 1.6 2.6-1.1a5.2 5.2 0 1 0-2 4.1" fill="none" stroke="#fff" stroke-width="1.8" stroke-linecap="round"/>
        </svg>
        corwin@plumvexa.com
      </li>
      <li class="contact-item">
        <svg class="contact-icon" viewBox="0 0 24 24" aria-hidden="true">
          <circle cx="12" cy="12" r="12" fill="var(--accent-red)"/>
          <circle cx="12" cy="12" r="6" fill="none" stroke="#fff" stroke-width="1.5"/>
          <ellipse cx="12" cy="12" rx="2.6" ry="6" fill="none" stroke="#fff" stroke-width="1.3"/>
          <line x1="6" y1="12" x2="18" y2="12" stroke="#fff" stroke-width="1.3"/>
        </svg>
        www.plumvexa.com
      </li>
    </ul>

    <div class="person">
      <p class="person-name">Corwin Hask</p>
      <p class="person-title">Certified Appraiser</p>
    </div>
  </section>
</main>
</body>
</html>
```